Awesome photographers card for an awesome new business

Double sided business card Black background and silver logo in middle on one side. Details on otherside. please keep it simple

Photographer

Gavin Tolley
0482615073
GavinTolleyPhotography82@lumenpost.com
www.GavinTolleyPhotography.com.au
Instagram _Gavin_tolley

Requirements
Must have
• My logo in Silver
• please use instagram logo instead of "Instagram"

```html
<!DOCTYPE html>
<html lang="en">
<head>
<meta charset="utf-8">
<title>Gavin Tolley – Business Card</title>
<link rel="stylesheet" href="https://fonts.googleapis.com/css2?family=Open+Sans:wght@400;600&display=swap">
<style>
  :root {
    --backdrop: #6e4b34;
    --card: #0b0b0b;
    --silver: #c9c9c9;
    --silver-dim: #a9a9a9;
    --text: #bdbdbd;
  }
  html, body {
    margin: 0;
    padding: 0;
    width: 1200px;
    height: 1000px;
    overflow: hidden;
    background: var(--backdrop);
    font-family: "Open Sans", Arial, sans-serif;
  }
  .canvas {
    position: relative;
    width: 1200px;
    height: 1000px;
  }
  .card {
    position: absolute;
    left: 267px;
    width: 665px;
    height: 397px;
    background: var(--card);
    box-shadow: 0 2px 6px rgba(0,0,0,0.45);
  }
  .card--front { top: 74px; }
  .card--back { top: 533px; }

  .brand {
    position: absolute;
    left: 333px;
    top: 186px;
    transform: translate(-50%, -50%);
    width: 260px;
    height: 260px;
  }
  .brand__ring {
    position: absolute;
    inset: 0;
  }
  .brand__name {
    position: absolute;
    left: 0;
    right: 0;
    top: 50%;
    transform: translateY(-50%);
    margin: 0;
    text-align: center;
    font-size: 26px;
    font-weight: 600;
    letter-spacing: 3px;
    color: var(--silver);
    text-transform: uppercase;
  }

  .details {
    position: absolute;
    left: 32px;
    top: 108px;
    color: var(--text);
  }
  .details__name {
    margin: 0;
    font-size: 22px;
    font-weight: 600;
    letter-spacing: 0.3px;
    color: var(--silver-dim);
    line-height: 30px;
    text-transform: uppercase;
  }
  .details__role {
    margin: 0;
    font-size: 14px;
    line-height: 20px;
    color: var(--text);
  }
  .contact {
    list-style: none;
    margin: 48px 0 0;
    padding: 0;
    font-size: 14.5px;
    line-height: 23px;
  }
  .contact__item {
    display: flex;
    align-items: center;
    gap: 7px;
  }
  .contact__icon {
    width: 13px;
    height: 13px;
    flex: none;
    fill: var(--silver-dim);
  }
</style>
</head>
<body>
<main class="canvas">
  <section class="card card--front" aria-label="Card front">
    <div class="brand">
      <svg class="brand__ring" viewBox="0 0 260 260" aria-hidden="true">
        <circle cx="130" cy="130" r="122" fill="none" stroke="#c9c9c9" stroke-width="4"/>
      </svg>
      <p class="brand__name">Gavin Tolley</p>
    </div>
  </section>

  <section class="card card--back" aria-label="Card back">
    <div class="details">
      <h1 class="details__name">Gavin Tolley</h1>
      <p class="details__role">Photographer</p>
      <ul class="contact">
        <li class="contact__item">
          <svg class="contact__icon" viewBox="0 0 16 16" aria-hidden="true"><path d="M3.6 1.2l2.3 2.8-1.3 1.8c.9 2 2.5 3.6 4.5 4.6l1.8-1.3 2.8 2.3-1.2 2.6C7.2 13.8 2.2 8.8 1 3z"/></svg>
          <span>0482615073</span>
        </li>
        <li class="contact__item">
          <svg class="contact__icon" viewBox="0 0 16 16" aria-hidden="true"><rect x="2" y="2" width="12" height="12" rx="2"/></svg>
          <span>Gavin_tolley</span>
        </li>
        <li class="contact__item">
          <svg class="contact__icon" viewBox="0 0 16 16" aria-hidden="true"><path d="M1 3h14v10H1z M1 3l7 5.5L15 3" stroke="#0b0b0b" stroke-width="1"/></svg>
          <span>GavinTolleyPhotography82@lumenpost.com</span>
        </li>
        <li class="contact__item">
          <svg class="contact__icon" viewBox="0 0 16 16" aria-hidden="true"><circle cx="8" cy="8" r="6.5" fill="none" stroke="#a9a9a9" stroke-width="1.5"/><path d="M1.5 8h13M8 1.5c-3 3.5-3 9.5 0 13M8 1.5c3 3.5 3 9.5 0 13" fill="none" stroke="#a9a9a9" stroke-width="1.2"/></svg>
          <span>www.GavinTolleyPhotography.com.au</span>
        </li>
      </ul>
    </div>
  </section>
</main>
</body>
</html>
```